Kestrel Homes Australia Business Card

We need a Business Card design for our new start up company.
A unique model designed to address Australia’s growing housing affordability problem has been launched. More than half of Australians are being priced out of the property market and have resigned themselves to the fact that they may never be able to afford a home.
We have developed a unique Algorithm that allows people to get into property and reverse this trend of domination by the property investors in this country. The first of its kind model facilitates connecting people to lending facilities that do not require them to have the finance combined under the purchase contract.
Ownership is shared with a second-tier investor, made up of either family or friends if not, Kestrel Homes Australia will provide a mini property investor enabling thousands of people the opportunity to buy a home, which they otherwise thought was not possible.
Kestrel Homes Australia is addressing housing affordability for families and individuals, giving every Australian looking to buy a home the opportunity to enter the property market to live in or invest.
Under our unique model, there is no combined finance, and individuals are assessed for their percentage portion of the property only. “A unique feature of our product is it is based around the strategies used for property investment. I have developed a unique Algorithm that enables the Home buyer to purchase 60% of a property, while Kestrel Homes Australia facilitates a second-tier investor to buy the other 40%. The Algorithm locks the investor in place and enables the home buyer to stairway to full ownership. The investment is secured against real property.
Please refer to our website www.kestrelhomes.com.au for inspiration.
Also please find attached our logo.
Any further directions please ask.
Cheers Marcus
Industry/Entity Type
Real Estate
Contact Information for Business Card
Marcus Thorley
CEO
Mobile 0400 615 272
www.kestrelhomes.com.au
Email: marcus@kestrelhomes.com.au
Colors
Designer to choose colors to be used in the design.
Look and feel

```html
<!DOCTYPE html>
<html lang="en">
<head>
<meta charset="UTF-8">
<title>Kestrel Homes Australia – Business Card</title>
<link rel="stylesheet" href="https://fonts.googleapis.com/css2?family=Open+Sans:wght@400;600;700&display=swap">
<style>
  :root {
    --stage: #0b0b0b;
    --card: #f8f6f1;
    --green: #27a54a;
    --teal: #1aa3c9;
    --ink: #2b2f2c;
    --radius: 14px;
  }
  * { box-sizing: border-box; margin: 0; padding: 0; }
  html, body { width: 1200px; height: 1000px; overflow: hidden; }
  body {
    position: relative;
    background: var(--stage);
    font-family: "Open Sans", Arial, sans-serif;
  }
  .card {
    position: absolute;
    width: 540px;
    height: 309px;
    background: var(--card);
    border-radius: var(--radius);
    overflow: hidden;
  }
  .card--front { left: 50px; top: 190px; }
  .card--back { left: 610px; top: 500px; }

  /* Front */
  .front-brand {
    position: absolute;
    inset: 0;
    display: flex;
    flex-direction: column;
    align-items: center;
    justify-content: center;
    gap: 8px;
  }
  .brand-name {
    font-weight: 700;
    font-size: 25px;
    color: var(--teal);
    letter-spacing: 0.2px;
    display: flex;
    align-items: center;
    gap: 10px;
  }
  .brand-dot {
    width: 14px; height: 14px;
    border-radius: 50%;
    background: var(--green);
  }
  .brand-tagline {
    font-weight: 600;
    font-size: 13px;
    color: var(--green);
    letter-spacing: 0.3px;
  }

  /* Back */
  .back-panel { position: absolute; inset: 0; width: 100%; height: 100%; }
  .contact {
    position: absolute;
    left: 24px;
    top: 108px;
    color: var(--ink);
  }
  .contact-name { font-weight: 700; font-size: 17px; line-height: 1.2; }
  .contact-role { font-size: 14px; margin-bottom: 12px; }
  .contact-list { list-style: none; display: flex; flex-direction: column; gap: 4px; }
  .contact-list li {
    display: flex; align-items: center; gap: 8px;
    font-size: 12.5px;
  }
  .contact-list svg { width: 13px; height: 13px; fill: var(--ink); flex: none; }
  .back-brand {
    position: absolute;
    left: 285px;
    right: 15px;
    top: 0; bottom: 0;
    display: flex;
    align-items: center;
    justify-content: center;
    text-align: center;
  }
  .back-brand .brand-name { font-size: 18px; }
</style>
</head>
<body>
  <section class="card card--front" aria-label="Business card front">
    <div class="front-brand">
      <div class="brand-name"><span class="brand-dot"></span>Kestrel Homes Australia</div>
      <div class="brand-tagline">Shared Paths To Owning Your Home</div>
    </div>
  </section>

  <section class="card card--back" aria-label="Business card back">
    <svg class="back-panel" viewBox="0 0 540 309" preserveAspectRatio="none" aria-hidden="true">
      <path fill="var(--green)" d="M0 0 H275 L258 150 L250 152 L246 186 L240 188 L232 309 H0 Z"/>
    </svg>
    <div class="contact">
      <div class="contact-name">Marcus Thorley</div>
      <div class="contact-role">CEO</div>
      <ul class="contact-list">
        <li>
          <svg viewBox="0 0 24 24"><path d="M6.6 10.8a15.1 15.1 0 0 0 6.6 6.6l2.2-2.2c.3-.3.7-.4 1-.2 1.1.4 2.3.6 3.6.6.6 0 1 .4 1 1V20c0 .6-.4 1-1 1A17 17 0 0 1 3 4c0-.6.4-1 1-1h3.5c.6 0 1 .4 1 1 0 1.3.2 2.5.6 3.6.1.3 0 .7-.2 1z"/></svg>
          0400 615 272
        </li>
        <li>
          <svg viewBox="0 0 24 24"><path d="M2 5h20v14H2z M2 5l10 8 10-8" fill="none" stroke="var(--ink)" stroke-width="2"/><path d="M3 6l9 7 9-7v0H3z"/></svg>
          www.kestrelhomes.com.au
        </li>
        <li>
          <svg viewBox="0 0 24 24"><circle cx="12" cy="12" r="9.5" fill="none" stroke="var(--ink)" stroke-width="2"/><path d="M2.5 12h19M12 2.5c3 3 3 16 0 19M12 2.5c-3 3-3 16 0 19" fill="none" stroke="var(--ink)" stroke-width="1.6"/></svg>
          marcus@kestrelhomes.com.au
        </li>
      </ul>
    </div>
    <div class="back-brand">
      <div class="brand-name">Kestrel Homes Australia</div>
    </div>
  </section>
</body>
</html>
```